Ebook Design for Halvora Biosciences (Health and Dietary Supplements)

Halvora Biosciences is an exciting new company in the area of health and wellness. Health requires a multi-dimensional, interdisciplinary approach that encompasses a complete lifestyle. Our company believes in whole-health that incorporates the entire body to ultimately help you live better and longer. We invest in products that boost metabolic functions, enhance natural performance, and support a healthy lifespan. We need a design for our research eBook on our products that sticks true to our brand identity. Please use the colors royal blue and yellow.

```html
<!DOCTYPE html>
<html lang="en">
<head>
<meta charset="utf-8">
<title>Halvora Biosciences – Research eBook Layout</title>
<link rel="stylesheet" href="https://fonts.googleapis.com/css2?family=Montserrat:wght@400;600;700;800&family=Oswald:wght@600;700&family=Open+Sans:wght@400;600&display=swap">
<style>
  :root{
    --royal:#2b56e0;
    --sun:#f7d000;
    --sun-soft:#ffe233;
    --ink:#111111;
    --paper:#ffffff;
    --backdrop:#c3c3c3;
    --text:#222222;
    --photo-light:#b4dcef;
    --photo-warm:#d9c4a4;
  }
  *{box-sizing:border-box;margin:0;padding:0}
  html,body{width:874px;height:1200px;overflow:hidden;background:var(--backdrop)}
  .stage{position:absolute;left:0;top:0;width:1092px;height:1500px;transform:scale(.8);transform-origin:0 0;font-family:"Montserrat",sans-serif;color:var(--text)}
  .page{position:absolute;width:459px;height:649px;overflow:hidden;background:linear-gradient(135deg,#ffffff 0%,#ececec 55%,#f6f6f6 100%);box-shadow:0 2px 6px rgba(0,0,0,.25)}
  .page--front{left:56px;top:37px}
  .page--quote{left:571px;top:37px}
  .page--contents{left:56px;top:772px}
  .page--back{left:571px;top:772px}
  .shapes{position:absolute;inset:0;width:459px;height:649px}
  .caption{position:absolute;width:459px;text-align:center;font-family:"Open Sans",sans-serif;font-size:28px;color:#1a1a1a;letter-spacing:.5px}
  .caption--front{left:56px;top:702px}
  .caption--quote{left:571px;top:702px}
  .caption--contents{left:56px;top:1436px}
  .caption--back{left:571px;top:1436px}
  .logo-box{position:absolute;border:1.5px solid var(--ink);font-weight:700;color:var(--ink);display:flex;align-items:center;justify-content:center;text-align:center;background:var(--paper)}
  .front-logo{left:148px;top:41px;width:164px;height:48px;font-size:25px}
  .photo{position:absolute}
  .photo--clinic{inset:0;background:linear-gradient(120deg,#555 0%,#9a9a9a 45%,#c4c4c4 60%,#666 100%);clip-path:polygon(0 153px,459px 153px,459px 190px,312px 440px,0 440px)}
  .photo--beach{left:0;top:0;width:459px;height:517px;background:linear-gradient(180deg,var(--photo-light) 0%,var(--photo-warm) 100%)}
  .cover-title{position:absolute;left:21px;top:258px;color:var(--paper)}
  .cover-title__main{font-family:"Oswald",sans-serif;font-weight:700;font-size:44px;line-height:1;letter-spacing:.5px;text-transform:uppercase}
  .cover-title__sub{font-weight:800;font-size:26px;line-height:1.1;margin-top:4px;text-transform:uppercase}
  .intro{position:absolute;left:22px;top:508px;width:234px}
  .intro__head{font-weight:700;font-size:15px;color:var(--ink);display:flex;align-items:center;gap:8px}
  .intro__body{font-family:"Open Sans",sans-serif;font-size:8.2px;line-height:1.38;text-align:justify;margin-top:6px;color:#222}
  .web{position:absolute;top:610px;font-size:8px;letter-spacing:2px;color:#222;display:flex;align-items:center;gap:5px;font-family:"Open Sans",sans-serif}
  .web--right{left:307px}
  .web--left{left:22px}
  .quote-mark{position:absolute;left:51px;top:255px;width:66px;height:88px;background:var(--sun);color:var(--paper);font-family:"Montserrat",sans-serif;font-weight:800;font-size:70px;line-height:1;padding:20px 0 0 10px}
  .quote-lead{position:absolute;left:62px;top:361px;width:205px;color:var(--paper);font-weight:600;font-size:14.5px;line-height:1.45}
  .quote-rule{position:absolute;left:62px;top:459px;width:45px;height:3px;background:var(--paper)}
  .quote-body{position:absolute;left:59px;top:487px;width:204px;color:var(--paper);font-family:"Open Sans",sans-serif;font-size:8.2px;line-height:1.7;text-align:justify}
  .toc-card{position:absolute;left:62px;top:51px;width:336px;height:508px;background:var(--paper);border:3px solid var(--sun)}
  .toc-title{position:absolute;left:34px;top:20px}
  .toc-title__small{font-weight:700;font-size:19px;color:var(--ink)}
  .toc-title__big{font-weight:800;font-size:30px;color:var(--royal);line-height:1.1}
  .toc-list{position:absolute;left:34px;top:118px;width:181px;list-style:none}
  .toc-list li{height:41.7px;border-bottom:1.5px solid var(--royal);font-family:"Open Sans",sans-serif;font-size:12px;color:var(--ink);padding-top:5px;white-space:nowrap}
  .toc-pages{position:absolute;left:280px;top:118px;list-style:none;font-weight:700;font-size:12px;color:var(--ink)}
  .toc-pages li{height:27.8px}
  .contact-tag{position:absolute;left:138px;top:162px;width:168px;height:50px;background:var(--sun);color:var(--paper);font-weight:700;font-size:22px;display:flex;align-items:center;justify-content:center;letter-spacing:.3px}
  .company{position:absolute;left:135px;top:234px;color:var(--sun);font-weight:700;font-size:20px;white-space:nowrap}
  .company-rule{position:absolute;left:135px;top:268px;width:44px;height:3px;background:var(--sun)}
  .contact-list{position:absolute;left:136px;top:290px;list-style:none;color:var(--paper);font-family:"Open Sans",sans-serif;font-size:8.2px}
  .contact-list li{height:22px;display:flex;align-items:center;gap:6px}
  .contact-note{position:absolute;left:135px;top:384px;width:262px;color:var(--paper);font-family:"Open Sans",sans-serif;font-size:8px;line-height:1.4}
  .back-intro{position:absolute;left:21px;top:508px;width:234px}
  .back-intro__head{font-weight:700;font-size:15px;color:var(--royal)}
  .back-logo{left:322px;top:500px;width:90px;height:82px;font-size:26px;line-height:1.4}
</style>
</head>
<body>
<div class="stage">

  <section class="page page--front" aria-label="Front cover">
    <div class="photo photo--clinic" role="img" aria-label="Black and white photo of a patient's arm during a blood pressure check"></div>
    <svg class="shapes" viewBox="0 0 459 649" aria-hidden="true">
      <polygon points="0,129 328,129 312,153 0,153" fill="var(--royal)"/>
      <polygon points="459,178 459,527 282,527" fill="var(--sun)"/>
      <polygon points="0,224 294,224 252,370 0,370" fill="var(--sun)"/>
      <polygon points="326,200 342,200 188,464 172,464" fill="var(--royal)"/>
      <polygon points="0,440 178,440 165,464 0,464" fill="var(--royal)"/>
      <rect x="0" y="613" width="298" height="4" fill="var(--royal)"/>
    </svg>
    <div class="logo-box front-logo">LOGO HERE</div>
    <h1 class="cover-title">
      <div class="cover-title__main">Halvora</div>
      <div class="cover-title__sub">Biosciences</div>
    </h1>
    <div class="intro">
      <div class="intro__head">
        <svg width="17" height="15" viewBox="0 0 17 15" aria-hidden="true"><rect x="1" y="3" width="11" height="11" fill="none" stroke="var(--sun)" stroke-width="1.8"/><path d="M8 8 L16 1 M11 1 H16 V6" fill="none" stroke="var(--sun)" stroke-width="1.8"/></svg>
        LOREM IPSUM
      </div>
      <p class="intro__body">Lorem Ipsum is simply dummy text of the printing and typesetting industry. Lorem Ipsum has been the industry's standard dummy text ever since the 1500s, when an unknown printer took a galley of type and scrambled.</p>
    </div>
    <div class="web web--right"><svg width="9" height="9" viewBox="0 0 10 10" aria-hidden="true"><circle cx="5" cy="5" r="4.5" fill="#333"/><path d="M0.5 5 H9.5 M5 0.5 V9.5" stroke="#fff" stroke-width=".8"/></svg>www.webaddress.com</div>
  </section>
  <div class="caption caption--front">FRONT COVER</div>

  <section class="page page--quote" aria-label="Page 01">
    <div class="photo photo--beach" role="img" aria-label="Photo of a woman leaping joyfully on a sunny beach"></div>
    <svg class="shapes" viewBox="0 0 459 649" aria-hidden="true">
      <polygon points="32,253 289,303 289,593 32,593" fill="#ececec"/>
      <polygon points="42,263 279,308 279,583 42,583" fill="var(--royal)"/>
      <rect x="163" y="613" width="296" height="4" fill="var(--royal)"/>
    </svg>
    <div class="quote-mark">“</div>
    <p class="quote-lead">Lorem Ipsum is simply dummy text of the printing and typesetting industry. Lorem Ipsum has been.</p>
    <div class="quote-rule"></div>
    <p class="quote-body">Lorem Ipsum is simply dummy text of the printing and typesetting industry. Lorem Ipsum has been the industry's standard dummy text ever since the 1500s, when an unknown printer took a galley of type and scrambled.</p>
    <div class="web web--left"><svg width="9" height="9" viewBox="0 0 10 10" aria-hidden="true"><circle cx="5" cy="5" r="4.5" fill="#333"/><path d="M0.5 5 H9.5 M5 0.5 V9.5" stroke="#fff" stroke-width=".8"/></svg>www.webaddress.com</div>
  </section>
  <div class="caption caption--quote">PAGE - 01</div>

  <section class="page page--contents" aria-label="Page 02">
    <svg class="shapes" viewBox="0 0 459 649" aria-hidden="true">
      <rect x="0" y="139" width="459" height="371" fill="var(--sun)"/>
      <rect x="0" y="613" width="298" height="4" fill="var(--royal)"/>
    </svg>
    <div class="toc-card">
      <h2 class="toc-title">
        <div class="toc-title__small">TABLE OF</div>
        <div class="toc-title__big">CONTENTS</div>
      </h2>
      <ul class="toc-list">
        <li>Lorem Ipsum is simply dummy</li>
        <li>Lorem Ipsum is simply dummy</li>
        <li>Lorem Ipsum is simply dummy</li>
        <li>Lorem Ipsum is simply dummy</li>
        <li>Lorem Ipsum is simply dummy</li>
        <li>Lorem Ipsum is simply dummy</li>
        <li>Lorem Ipsum is simply dummy</li>
        <li>Lorem Ipsum is simply dummy</li>
      </ul>
      <ol class="toc-pages">
        <li>01</li><li>02</li><li>03</li><li>04</li><li>05</li><li>06</li>
        <li>07</li><li>08</li><li>09</li><li>10</li><li>11</li><li>12</li>
      </ol>
    </div>
    <div class="web web--right"><svg width="9" height="9" viewBox="0 0 10 10" aria-hidden="true"><circle cx="5" cy="5" r="4.5" fill="#333"/><path d="M0.5 5 H9.5 M5 0.5 V9.5" stroke="#fff" stroke-width=".8"/></svg>www.webaddress.com</div>
  </section>
  <div class="caption caption--contents">PAGE - 02</div>

  <section class="page page--back" aria-label="Back cover">
    <svg class="shapes" viewBox="0 0 459 649" aria-hidden="true">
      <defs>
        <linearGradient id="sunFade" x1="0" y1="0" x2="1" y2="1">
          <stop offset="0" stop-color="var(--sun-soft)"/>
          <stop offset="1" stop-color="var(--sun)"/>
        </linearGradient>
      </defs>
      <polygon points="0,0 178,0 0,345" fill="url(#sunFade)"/>
      <polygon points="167,68 186,68 49,333 30,333" fill="var(--royal)"/>
      <polygon points="339,129 459,129 459,154 327,154" fill="var(--royal)"/>
      <polygon points="151,154 459,154 459,440 11,440" fill="var(--ink)"/>
      <rect x="424" y="224" width="35" height="145" fill="var(--royal)"/>
      <polygon points="177,440 459,440 459,464 164,464" fill="var(--royal)"/>
      <rect x="163" y="613" width="296" height="4" fill="var(--royal)"/>
    </svg>
    <div class="contact-tag">CONTACT US</div>
    <div class="company">Lorem Ipsum Company.inc</div>
    <div class="company-rule"></div>
    <ul class="contact-list">
      <li><svg width="9" height="9" viewBox="0 0 10 10" aria-hidden="true"><circle cx="5" cy="5" r="5" fill="#fff"/><path d="M5 2 a2 2 0 0 1 2 2 c0 1.5 -2 4 -2 4 s-2 -2.5 -2 -4 a2 2 0 0 1 2 -2z" fill="#111"/></svg>Lorem Ipsum is simply dummy text of the printing</li>
      <li><svg width="9" height="9" viewBox="0 0 10 10" aria-hidden="true"><circle cx="5" cy="5" r="5" fill="#fff"/><path d="M3 2.5 l1.2 0 .5 1.5 -.8 .6 a4 4 0 0 0 1.6 1.6 l.6 -.8 1.5 .5 0 1.2 a4.5 4.5 0 0 1 -4.6 -4.6z" fill="#111"/></svg>022 - 1234 - 5678</li>
      <li><svg width="9" height="9" viewBox="0 0 10 10" aria-hidden="true"><circle cx="5" cy="5" r="5" fill="#fff"/><path d="M3 2.5 l1.2 0 .5 1.5 -.8 .6 a4 4 0 0 0 1.6 1.6 l.6 -.8 1.5 .5 0 1.2 a4.5 4.5 0 0 1 -4.6 -4.6z" fill="#111"/></svg>022 - 1234 - 5678</li>
      <li><svg width="9" height="9" viewBox="0 0 10 10" aria-hidden="true"><circle cx="5" cy="5" r="5" fill="#fff"/><rect x="2.5" y="3.3" width="5" height="3.4" fill="#111"/><path d="M2.5 3.3 L5 5.3 L7.5 3.3" stroke="#fff" stroke-width=".6" fill="none"/></svg>info@emailaddress.com</li>
    </ul>
    <p class="contact-note">Lorem Ipsum is simply dummy text of the printing and typesetting industry. Lorem Ipsum has been the industry's standard dummy text ever since the 1500s.</p>
    <div class="back-intro">
      <div class="back-intro__head">LOREM IPSUM</div>
      <p class="intro__body">Lorem Ipsum is simply dummy text of the printing and typesetting industry. Lorem Ipsum has been the industry's standard dummy text ever since the 1500s, when an unknown printer took a galley of type and scrambled.</p>
    </div>
    <div class="logo-box back-logo">LOGO<br>HERE</div>
    <div class="web web--left"><svg width="9" height="9" viewBox="0 0 10 10" aria-hidden="true"><circle cx="5" cy="5" r="4.5" fill="#333"/><path d="M0.5 5 H9.5 M5 0.5 V9.5" stroke="#fff" stroke-width=".8"/></svg>www.webaddress.com</div>
  </section>
  <div class="caption caption--back">BACK COVER</div>

</div>
</body>
</html>
```